Create modern and sleek business card for luxury real estate company

We're a "boutique" real estate office looking for a design that gets across a highly modern luxury brand. Blacks and whites are probably the best colors unless we try a silver foil for the logo. I've attached a version of our current logo here. I'd like to swap out the current font on there with Gotham Light Regular.

I'm looking to have one side of the card have the logo with the space for our agents info on the other side.

Target Market(s)

Young professionals in a "luxury" headspace

Industry/Entity Type

Real estate

Contact Information for Business Card

A place for agent name, cell number, website. The slogan "Simply Rethinking Real Estate".

Font styles to use
Other font styles liked:
• Gotham Regular

Colors

Designer to choose only greyscale colors for use in the design.

Requirements
Must have
• Matte black as the background color. Clean lines and use of contrast. A specific design aspect that will use silver foil.
Nice to have
• Up in the air on integrating a QR code
Should not have
• Any houses or other real estate related design (ex: a clip art house)

```html
<!DOCTYPE html>
<html lang="en">
<head>
<meta charset="utf-8">
<title>Vesper Realty – Business Card</title>
<link href="https://fonts.googleapis.com/css2?family=Montserrat:wght@300;400&display=swap" rel="stylesheet">
<style>
  :root {
    --stage: #000000;
    --card: #404040;
    --ink-light: #d9d9d9;
    --ink-soft: #cfcfcf;
    --ink-dark: #2e2e2e;
    --name-start: #2c2c2c;
    --name-end: #ffffff;
  }
  * { margin: 0; padding: 0; box-sizing: border-box; }
  html, body {
    width: 1200px; height: 1200px; overflow: hidden;
    background: var(--stage);
    font-family: "Montserrat", Arial, sans-serif;
    font-weight: 300;
  }
  .card {
    position: absolute;
    width: 457px; height: 258px;
    background: var(--card);
    border-radius: 24px;
  }
  .card--front { left: 366px; top: 293px; }
  .card--back  { left: 377px; top: 647px; }

  .agent-name {
    position: absolute; left: 0; right: 0; top: 32px;
    text-align: center;
    font-size: 42px; font-weight: 400; letter-spacing: 0.5px;
    background: linear-gradient(90deg, var(--name-start) 0%, var(--name-start) 38%, var(--name-end) 80%);
    -webkit-background-clip: text; background-clip: text;
    color: transparent;
    padding-left: 2px;
  }
  .contact {
    position: absolute; top: 105px;
    font-size: 13.5px; line-height: 14.9px; letter-spacing: 1.2px;
    color: var(--ink-soft);
    white-space: nowrap;
  }
  .contact--phones { left: 41px; }
  .contact--web { left: 207px; }

  .brand {
    position: absolute; left: 41px; top: 166px;
    display: flex; align-items: center; gap: 29px;
  }
  .brand__square { width: 50px; height: 50px; flex: none; }
  .brand__name {
    font-size: 28px; line-height: 31px; letter-spacing: 1.5px;
    font-weight: 300;
  }
  .card--front .brand__square { background: var(--ink-dark); }
  .card--front .brand__name { color: var(--ink-dark); }
  .card--back .brand__square { background: var(--ink-light); }
  .card--back .brand__name { color: var(--ink-light); }
</style>
</head>
<body>
  <section class="card card--front">
    <h1 class="agent-name">John Doe</h1>
    <p class="contact contact--phones">P . 310 482 915<br>M. 310 482 916<br>F . 310 482 917</p>
    <p class="contact contact--web">E . vesper@realtyco.com<br>&nbsp;Elm street&nbsp; No. 4 VR</p>
    <div class="brand">
      <span class="brand__square"></span>
      <span class="brand__name">VESPER<br>REALTY</span>
    </div>
  </section>

  <section class="card card--back">
    <div class="brand">
      <span class="brand__square"></span>
      <span class="brand__name">VESPER<br>REALTY</span>
    </div>
  </section>
</body>
</html>
```